Mobile Recording Studio needs business cards

Open to seeing a creative design, but I want to emphasis my logo and minimize the name/title and company information. Possible a fully black background on card.

My company is a mobile sound recording studio. ok to include a my trailer (actual or cartoon) on the card. My initial thought is more straight forward, but a good design will win me over.

SPECS:
CMYK color mode
High (300ppi) raster effect.
cover bleed area
please deliver: Illustrator file with layers and a pdf at completion.

Name and info for the business card:

Mitchell Garvey
ADR Mixer

email: Mitchell@TakebayDub.example

address:
418 - 6057 East Pembury
Vancouver, BC V3R 2T4

phone:
604.419.8827 office

website:
www.TakebayDub.example

FB: @TakebayDub

Instagram: @TheTakebayDub

Industry/Entity Type

Television Production

Contact Information for Business Card

Mitchell Garvey
ADR Mixer

email: Mitchell@TakebayDub.example

address:
418 - 6057 East Pembury
Vancouver, BC V3R 2T4

phone:
604.419.8827 office

website:
www.TakebayDub.example

FB: @TakebayDub

Instagram: @TheTakebayDub

Colors

Designer to choose colors to be used in the design.

Requirements
Must have
• emphasis my logo and minimize the name/title and company information.
• SPECS:
• CMYK color mode
• High (300ppi) raster effect.
• cover bleed area
• please deliver: Illustrator file with layers and a pdf at completion.
Nice to have
• maybe include the following:
• all black background or black theme
• my work trailer (actual or cartoon) refer to Instagram: @TheTakebayDub

```html
<!DOCTYPE html>
<html lang="en">
<head>
<meta charset="utf-8">
<title>Takebay Dub – Business Card</title>
<link rel="stylesheet" href="https://fonts.googleapis.com/css2?family=Montserrat:wght@400;500&display=swap">
<style>
  :root {
    --backdrop: #5e5042;
    --card-black: #050505;
    --ink-white: #f4f4f4;
    --ink-grey: #9a9a9a;
    --rule: #5a5a5a;
    --silver-light: #e6e6e6;
    --silver-mid: #a9a9a9;
    --silver-dark: #3e3e3e;
    --photo-dark: #2a2338;
    --photo-mid: #5b5072;
    --photo-light: #b9b7c4;
    --back-top: #5f5f5f;
    --back-bottom: #2f2f2f;
  }
  * { box-sizing: border-box; margin: 0; padding: 0; }
  html, body { width: 900px; height: 1200px; overflow: hidden; }
  body {
    background: var(--backdrop);
    font-family: "Montserrat", Arial, sans-serif;
    position: relative;
  }
  .card {
    position: absolute;
    left: 80px;
    width: 735px;
    height: 429px;
    border-radius: 22px;
    overflow: hidden;
  }

  /* Front */
  .card-front { top: 127px; background: var(--card-black); }
  .info-panel { position: absolute; left: 0; top: 0; width: 460px; height: 100%; padding: 58px 0 0 57px; }
  .person-name { color: var(--ink-white); font-size: 21px; font-weight: 400; letter-spacing: 0.3px; line-height: 1.1; }
  .person-title { color: var(--ink-grey); font-size: 15px; line-height: 1.3; margin-bottom: 9px; }
  .info-rule { width: 283px; height: 1px; background: var(--rule); margin: 12px 0 10px; }
  .contact-list { list-style: none; }
  .contact-item {
    display: flex; align-items: flex-start;
    color: var(--ink-white); font-size: 16px; line-height: 30px; letter-spacing: 0.2px;
  }
  .contact-icon { width: 22px; height: 22px; margin: 4px 12px 0 0; flex: none; }
  .contact-icon.blank { visibility: hidden; }
  .panel-divider {
    position: absolute; left: 460px; top: 0; width: 5px; height: 100%;
    background: linear-gradient(90deg, var(--silver-dark), var(--silver-light), var(--silver-dark));
  }
  .trailer-photo {
    position: absolute; left: 465px; top: 0; right: 0; height: 100%;
    background:
      linear-gradient(180deg, rgba(185,183,196,0.55) 0%, rgba(185,183,196,0) 35%),
      linear-gradient(160deg, var(--photo-mid) 0%, var(--photo-dark) 55%, #1c1826 100%);
  }

  /* Back */
  .card-back {
    top: 645px;
    background: linear-gradient(180deg, var(--back-top) 0%, #4a4a4a 55%, var(--back-bottom) 100%);
  }
  .brand-name {
    position: absolute; left: 0; right: 0; top: 150px;
    text-align: center;
    color: var(--silver-light);
    font-size: 64px; font-weight: 500; letter-spacing: 4px;
  }
  .base-band {
    position: absolute; left: 0; right: 0; top: 360px; height: 69px;
    background: linear-gradient(180deg, #8a8a8a 0%, #4c4c4c 20%, #3a3a3a 100%);
    border-top: 1px solid #bdbdbd;
  }
  .band-lights { position: absolute; left: 0; top: -8px; width: 100%; height: 18px; }
</style>
</head>
<body>

<section class="card card-front" aria-label="Business card front">
  <div class="info-panel">
    <p class="person-name">MITCHELL GARVEY</p>
    <p class="person-title">ADR Mixer</p>
    <p class="person-name">DALE REINHOLT</p>
    <p class="person-title">Engineer / Director of Operations</p>

    <div class="info-rule"></div>
    <ul class="contact-list">
      <li class="contact-item">
        <svg class="contact-icon" viewBox="0 0 22 22" aria-hidden="true">
          <circle cx="11" cy="11" r="10" fill="var(--silver-mid)"/>
          <path d="M6 8 q5 -4 10 0 l-1.5 2 h-2 v-1 h-3 v1 h-2 z M7 11 h8 v4 h-8 z" fill="#111"/>
        </svg>
        604.419.8827 (OFFICE)
      </li>
      <li class="contact-item">
        <svg class="contact-icon" viewBox="0 0 22 22" aria-hidden="true">
          <circle cx="11" cy="11" r="10" fill="var(--silver-mid)"/>
          <path d="M11 5 l6 5.5 h-2 v5.5 h-3 v-3 h-2 v3 h-3 v-5.5 h-2 z" fill="#111"/>
        </svg>
        <span>418 - 6057 East Pembury<br>Vancouver, BC V3R 2T4</span>
      </li>
    </ul>
    <div class="info-rule"></div>
    <ul class="contact-list">
      <li class="contact-item">
        <svg class="contact-icon" viewBox="0 0 22 22" aria-hidden="true">
          <circle cx="11" cy="11" r="10" fill="var(--silver-mid)"/>
          <g fill="none" stroke="#111" stroke-width="1.2">
            <circle cx="11" cy="11" r="6"/>
            <ellipse cx="11" cy="11" rx="2.6" ry="6"/>
            <path d="M5 11 h12 M6 8 h10 M6 14 h10"/>
          </g>
        </svg>
        www.TakebayDub.example
      </li>
      <li class="contact-item">
        <svg class="contact-icon" viewBox="0 0 22 22" aria-hidden="true">
          <circle cx="11" cy="11" r="10" fill="var(--silver-mid)"/>
        </svg>
        @TakebayDub
      </li>
      <li class="contact-item">
        <svg class="contact-icon" viewBox="0 0 22 22" aria-hidden="true">
          <circle cx="11" cy="11" r="10" fill="var(--silver-mid)"/>
        </svg>
        @TheTakebayDub
      </li>
    </ul>
  </div>
  <div class="panel-divider"></div>
  <div class="trailer-photo" role="img" aria-label="Photo of the company's branded mobile recording trailer parked outside a studio building"></div>
</section>

<section class="card card-back" aria-label="Business card back">
  <p class="brand-name">TAKEBAY DUB</p>
  <div class="base-band">
    <svg class="band-lights" viewBox="0 0 735 18" preserveAspectRatio="none" aria-hidden="true">
      <defs>
        <radialGradient id="glow">
          <stop offset="0" stop-color="#ffffff" stop-opacity="0.9"/>
          <stop offset="1" stop-color="#ffffff" stop-opacity="0"/>
        </radialGradient>
      </defs>
      <ellipse cx="140" cy="9" rx="22" ry="6" fill="url(#glow)"/>
      <ellipse cx="232" cy="9" rx="22" ry="6" fill="url(#glow)"/>
      <ellipse cx="352" cy="9" rx="22" ry="6" fill="url(#glow)"/>
      <ellipse cx="460" cy="9" rx="22" ry="6" fill="url(#glow)"/>
      <ellipse cx="560" cy="9" rx="22" ry="6" fill="url(#glow)"/>
      <ellipse cx="675" cy="9" rx="22" ry="6" fill="url(#glow)"/>
    </svg>
  </div>
</section>

</body>
</html>
```